Luxury Customizable Mattress Company Needs a Business Card that WOWs

I need a unique business card design that makes people stop... look and think WOW.

We are a new mattress company with our very own line of customizable beds (mattress & base) called the Trellis Rest. The innovation of our mattress is that the entire product is built of smaller components... once put together its a complete bed. It can be cleaned from the inside out. And it's a mattress made to share with a partner. As people's sleep needs are different, one person may prefer a water bed and a softer mattress while their partner may prefer a warm memory foam mattress with a firmer feel. Now they dont need to compromise, as the Trellis Rest allows each sleeper to get exactly what they need. And they can each change the feel of their side of the bed anytime with a click of a button.
check www.Trellisrest.example for more info (some pages do not work) Also check out our Clipora and Streamly videos.

We also opened up a new facility where people can try out our beds... called the Doze Harbor. This is a secondary business but we would like to have a small logo on the TR business card to highlight it. (dozeharbor.example)

Content on card....
Logo: Trellis Rest logo
Name: Miriam Okafor
Title: CEO & Sleep Enthusiast
Address: 4829 Varley Crescent Mississauga ON L5R 2T6 Canada
Telephone: 416.555.0193 (place holder .. this # will change)
Email: miriam@trellisrest.example
Web: www.trellisrest.example

Small Logo: Doze Harbor Logo
web: dozeharbor.example

Design: bold and modern, the design has a concept, if possible a card people can use (to ensure they keep the card) Ie. Sleep positions or NFC chip or something interesting. I am open to ideas and printing on unique materials... like soft vinyl fabric.

Target Market(s)

Mattress Consumers
Married Couples
Couples

Industry/Entity Type

Health And Wellness

Contact Information for Business Card

Logo: Trellis Rest logo
Name: Miriam Okafor
Web: www.trellisrest.example

SMALL Logo: Doze Harbor Logo
web: dozeharbor.example

Requirements
Must have
• bold and modern, the design has a concept, if possible a card people can use (to ensure they keep the card)
• ** I LIKE THIS CONCEPT: http://plovix.example/wp-content/uploads/2014/04/beautiful-creative-unique-original-impressive-business-cards-designs-18.jpg
• And the DESIGN I thought of has a silhouette of a woman sleeping on top of front of card and if you flip the card over there's a silhouette of a man sleeping on the bottom of the back of the card. IF you put 2 cards together (back to front) it looks like they are sleeping together.
• INSIDE pull out card can be designed later.
• See our website and videos for images we've used in the past.
• We are open to new concepts, images, stories.
• Must be story / people driven. Mattress sales are driven by the idea of good sleep, solving sleep issues and making people happy.
Nice to have
• Just some examples.... adding a feature to the card like a Sleep positions chart or NFC chip or something interesting. I am open to ideas and printing on unique materials... like soft vinyl fabric.
Should not have
• not dull in colour or concept

```html
<!DOCTYPE html>
<html lang="en">
<head>
<meta charset="utf-8">
<title>Trellis Rest — Business Card</title>
<link rel="stylesheet" href="https://fonts.googleapis.com/css2?family=Lato:wght@400;700&display=swap">
<style>
  :root {
    --stage: #acacac;
    --card-light: #f2f2f2;
    --card-dark: #232323;
    --card-dark-glow: #2d2d2d;
    --ink: #1a1a1a;
    --navy: #1f2a8a;
    --brand-blue: #0d62b4;
    --brand-blue-light: #2f86d6;
    --sky: #8fd3f2;
    --mark-tile: #8fd0f5;
    --mark-tile-deep: #5fb6ea;
  }
  * { box-sizing: border-box; margin: 0; padding: 0; }
  html, body { width: 1200px; height: 900px; overflow: hidden; }
  body {
    background: var(--stage);
    font-family: "Lato", Arial, sans-serif;
    position: relative;
  }
  .card {
    position: absolute;
    top: 200px;
    width: 310px;
    height: 502px;
    overflow: hidden;
  }
  .card--front {
    left: 265px;
    background: var(--card-light);
    border-radius: 62px 0 62px 0;
    color: var(--ink);
  }
  .card--back {
    left: 641px;
    width: 309px;
    background: var(--card-dark);
    border-radius: 0 62px 0 62px;
  }

  /* front: brand */
  .brand__tile {
    position: absolute;
    right: 20px;
    top: 30px;
    width: 186px;
    height: 100px;
    background: linear-gradient(180deg, var(--mark-tile-deep) 0%, var(--mark-tile) 100%);
  }
  .brand__name {
    position: absolute;
    right: 20px;
    top: 150px;
    font-size: 38px;
    font-weight: 400;
    line-height: 38px;
    color: var(--ink);
    text-align: right;
  }

  /* front: contact */
  .person {
    position: absolute;
    left: 34px;
    top: 291px;
  }
  .person__name {
    font-size: 19px;
    font-weight: 700;
    color: var(--navy);
    line-height: 24px;
  }
  .person__title {
    font-size: 13.5px;
    line-height: 20px;
  }
  .address {
    position: absolute;
    left: 34px;
    top: 353px;
    font-size: 13.5px;
    line-height: 18px;
    font-style: normal;
  }
  .contacts {
    position: absolute;
    left: 34px;
    top: 408px;
    list-style: none;
    font-size: 13.5px;
    line-height: 20.5px;
  }
  .contacts li { display: flex; align-items: center; gap: 8px; }
  .contacts svg { width: 10px; height: 10px; fill: var(--navy); flex: none; }

  /* back */
  .back-glow {
    position: absolute;
    left: 0;
    top: 0;
    width: 309px;
    height: 330px;
    background:
      radial-gradient(ellipse 170px 120px at 210px 90px, var(--card-dark-glow) 0%, transparent 100%),
      radial-gradient(ellipse 140px 110px at 90px 230px, var(--card-dark-glow) 0%, transparent 100%);
  }
  .sub-brand {
    position: absolute;
    left: 0;
    right: 0;
    top: 225px;
    display: flex;
    flex-direction: column;
    align-items: center;
  }
  .sub-brand__disc {
    width: 142px;
    height: 142px;
    border-radius: 50%;
    background: radial-gradient(circle at 40% 35%, var(--brand-blue-light) 0%, var(--brand-blue) 70%);
  }
  .sub-brand__name {
    margin-top: 4px;
    font-size: 22px;
    font-weight: 700;
    letter-spacing: 3px;
    color: var(--brand-blue);
    white-space: nowrap;
  }
  .sub-brand__by {
    align-self: flex-end;
    margin-right: 58px;
    font-size: 7px;
    color: var(--brand-blue);
    margin-top: -3px;
  }
  .sub-brand__web {
    margin-top: 12px;
    font-size: 16px;
    font-weight: 700;
    color: var(--sky);
  }
</style>
</head>
<body>
  <section class="card card--front">
    <span class="brand__tile" role="img" aria-label="Trellis Rest bed illustration area"></span>
    <span class="brand__name">Trellis<br>Rest</span>

    <div class="person">
      <p class="person__name">Miriam Okafor</p>
      <p class="person__title">CEO &amp; Sleep Enthusiast</p>
    </div>

    <address class="address">
      4829 Varley Crescent Mississauga<br>
      ON L5R 2T6 Canada
    </address>

    <ul class="contacts">
      <li>
        <svg viewBox="0 0 10 10" aria-hidden="true"><path d="M2 0.5 L3.6 2.6 L2.7 3.6 Q3.8 5.9 6.3 7.3 L7.4 6.4 L9.5 8 L8.3 9.5 Q3.5 9 0.5 1.7 Z"/></svg>
        416.555.0193
      </li>
      <li>
        <svg viewBox="0 0 10 10" aria-hidden="true"><path d="M0.5 2 H9.5 V8.5 H0.5 Z M0.5 2 L5 5.5 L9.5 2" stroke="#f2f2f2" stroke-width="0.8"/></svg>
        miriam@trellisrest.example
      </li>
      <li>
        <svg viewBox="0 0 10 10" aria-hidden="true"><circle cx="5" cy="5" r="4.6"/><path d="M2 4 Q4 3 5 5 Q6 7 7.5 6" stroke="#f2f2f2" stroke-width="0.9" fill="none"/></svg>
        www.trellisrest.example
      </li>
    </ul>
  </section>

  <section class="card card--back">
    <span class="back-glow" role="img" aria-label="Faint large brand decoration"></span>
    <div class="sub-brand">
      <span class="sub-brand__disc"></span>
      <span class="sub-brand__name">DOZE HARBOR</span>
      <span class="sub-brand__by">by Trellis Rest</span>
      <span class="sub-brand__web">www.dozeharbor.example</span>
    </div>
  </section>
</body>
</html>
```